2 Sided Stunning and Attention Getting Brochure

Create an eye-catching, 2 sided brochure. The first side of the brochure includes the content provided in the attached word document. Make it a look incredibly professional, modern, and unique. The second side of the brochure are frequently asked questions. They includes the content of both PDFs on one page.

Target Market(s)

Birch Toolworks Store Owners. People who own Birch Toolworks stores.

Industry/Entity Type

Retail

Font styles to use
Serif

Colors
EB3D1F
EC4F4E
F09395
F8D3D4
FCEDEE

Requirements
Must have
• Birch Toolworks colors. Red, white, and black. Must be super creative, modernized, and different. Must catch my attention immediately and I must say "Now that's different looking!" Include Birch Toolworks logo and Qelmar Group logo. Google these.
Should not have
• Boring and dull. It has to be super creative and different.

```html
<!DOCTYPE html>
<html lang="en">
<head>
<meta charset="utf-8">
<title>Electronic Shelf Labels Are Here</title>
<link href="https://fonts.googleapis.com/css2?family=DM+Serif+Display&family=Montserrat:wght@400;500;700;800&display=swap" rel="stylesheet">
<style>
:root{
  --red:#e31e3a;
  --red-deep:#c9182f;
  --pink:#f8d3d4;
  --ink:#1f1f1f;
  --text:#333;
  --grey-bg:#7a7a7a;
  --badge:#ececec;
  --box:#ececec;
  --serif:'DM Serif Display', Georgia, serif;
  --sans:'Montserrat', Arial, sans-serif;
}
*{margin:0;padding:0;box-sizing:border-box}
html,body{width:1200px;height:1200px;overflow:hidden}
body{background:var(--grey-bg);font-family:var(--sans);color:var(--text);position:relative}
.sheet{position:absolute;left:183px;top:99px;width:781px;height:1011px;background:#fff;overflow:hidden}
.side{position:absolute;left:0;top:0;width:233px;height:100%;background:linear-gradient(180deg,#fff 0%,#fdf3f3 35%,var(--pink) 75%,#f4b9bb 100%)}
.abs{position:absolute}

.badge{position:absolute;left:33px;top:29px;width:162px;height:162px;border-radius:50%;background:var(--badge);display:flex;align-items:center;justify-content:center;text-align:center}
.badge-name{font-family:var(--sans);font-weight:700;color:var(--red);font-size:20px;line-height:1.15}

.banner{position:absolute;left:184px;top:71px;width:572px;height:57px;background:linear-gradient(90deg,var(--red) 0%,var(--red-deep) 50%,var(--red) 100%);border-radius:0 29px 29px 0;color:#fff;font-family:var(--serif);font-size:35px;line-height:57px;padding-left:26px;letter-spacing:.2px}

.intro{left:255px;top:147px;width:505px;font-weight:800;font-size:13.2px;line-height:16.6px;color:var(--ink)}

.perk{position:absolute;font-size:11.9px;line-height:13.85px;color:var(--text)}
.perk.left{left:310px;width:192px}
.perk.right{left:564px;width:202px}
.icon{position:absolute;width:48px;height:48px}
.rail{position:absolute;width:0;border-left:1.2px dashed #999}

.h-costs{left:32px;top:248px;font-family:var(--serif);font-size:22px;color:var(--ink)}
.h-pricing{left:32px;top:277px;font-family:var(--serif);font-size:17px;color:var(--red)}
.tag{position:absolute;left:44px;width:147px;height:24px;background:var(--red);color:#fff;font-weight:800;font-size:12.5px;line-height:24px;padding-left:20px;clip-path:polygon(8px 0,100% 0,100% 100%,8px 100%,0 50%)}
.tag::before{content:"";position:absolute;left:7px;top:9px;width:6px;height:6px;border-radius:50%;background:#fff}
.string{position:absolute;left:30px;width:22px;height:30px}
.caption{position:absolute;left:54px;font-size:8.5px;color:var(--ink)}

.h-extra{left:33px;top:514px;width:190px;font-family:var(--serif);font-size:17px;line-height:19.5px;color:var(--red)}
.checks{left:33px;top:572px;width:192px;list-style:none;font-size:11.9px;line-height:13.85px;color:var(--ink)}
.checks>li{position:relative;padding-left:14px;margin-bottom:6px}
.checks>li::before{content:"";position:absolute;left:0;top:3px;width:9px;height:9px;border-radius:50%;background:var(--red)}
.sub{list-style:none;margin-top:6px}
.sub li{position:relative;padding-left:14px;margin-bottom:6px}
.sub li::before{content:"";position:absolute;left:3px;top:5px;width:4px;height:4px;border-radius:50%;background:var(--ink)}

.h-touch{left:32px;top:805px;width:200px;font-family:var(--serif);font-size:22px;line-height:24.5px;color:var(--ink)}
.contact-title{position:absolute;left:33px;font-family:var(--serif);font-size:12px;color:var(--red)}
.contact-line{position:absolute;left:33px;font-size:9px;font-weight:700;color:var(--ink);display:flex;align-items:center;gap:3px}
.contact-line svg{width:8px;height:8px}

.h-start{left:259px;top:740px;font-family:var(--serif);font-size:31px;color:var(--ink)}
.start-rule{position:absolute;left:480px;top:766px;width:260px;height:0;border-top:1.2px dashed #999}
.start-rule span{position:absolute;left:85px;top:-1.2px;width:85px;border-top:1.2px dashed var(--red)}
.step{position:absolute;background:var(--box);border-radius:14px;font-size:11.9px;line-height:13.85px;color:var(--ink);padding:11px 20px 0 24px}
.step-check{position:absolute;width:17px;height:17px}
</style>
</head>
<body>
<div class="sheet">
  <div class="side"></div>

  <div class="badge"><div class="badge-name">Birch<br>Toolworks</div></div>

  <div class="banner">Electronic Shelf Labels Are Here</div>

  <p class="abs intro">Introducing electronic shelf labels (ESLs) into your operations offers several benefits extending beyond just mere convenience. Below are the top reasons stores are investing in electronic shelf labels. ESLs:</p>

  <div class="rail" style="left:278px;top:268px;height:400px"></div>
  <div class="rail" style="left:533px;top:268px;height:395px"></div>

  <svg class="icon" style="left:254px;top:219px" viewBox="0 0 48 48"><circle cx="24" cy="24" r="22" fill="#fff" stroke="#222" stroke-width="1.5"/><path d="M24 2 A22 22 0 0 0 6 37" fill="none" stroke="#e31e3a" stroke-width="2.5"/><circle cx="27" cy="19" r="7" fill="none" stroke="#222" stroke-width="1.3"/><text x="27" y="23" font-size="10" text-anchor="middle" font-family="Arial" fill="#222">$</text><path d="M14 34v-8h4l3-6h2v6h5v8z" fill="none" stroke="#222" stroke-width="1.3"/></svg>
  <svg class="icon" style="left:254px;top:303px" viewBox="0 0 48 48"><circle cx="24" cy="24" r="22" fill="#fff" stroke="#222" stroke-width="1.5"/><path d="M24 46 A22 22 0 0 1 2 24" fill="none" stroke="#e31e3a" stroke-width="2.5"/><circle cx="24" cy="24" r="13" fill="none" stroke="#222" stroke-width="1.4"/><path d="M24 16v8l5 3" fill="none" stroke="#222" stroke-width="1.4"/></svg>
  <svg class="icon" style="left:254px;top:398px" viewBox="0 0 48 48"><circle cx="24" cy="24" r="22" fill="#fff" stroke="#222" stroke-width="1.5"/><path d="M2 24 A22 22 0 0 0 24 46" fill="none" stroke="#e31e3a" stroke-width="2.5"/><rect x="15" y="12" width="18" height="24" fill="none" stroke="#222" stroke-width="1.4"/><path d="M18 18h12M18 22h12M18 26h12M18 30h8" stroke="#222" stroke-width="1.2"/></svg>
  <svg class="icon" style="left:254px;top:496px" viewBox="0 0 48 48"><circle cx="24" cy="24" r="22" fill="#fff" stroke="#222" stroke-width="1.5"/><path d="M8 9 A22 22 0 0 0 24 46" fill="none" stroke="#e31e3a" stroke-width="2.5"/><path d="M13 20l3-7h16l3 7zM14 20v15h20V20M20 35v-8h8v8" fill="none" stroke="#222" stroke-width="1.3"/></svg>
  <svg class="icon" style="left:254px;top:581px" viewBox="0 0 48 48"><circle cx="24" cy="24" r="22" fill="#fff" stroke="#222" stroke-width="1.5"/><path d="M2 24 A22 22 0 0 0 24 46" fill="none" stroke="#e31e3a" stroke-width="2.5"/><rect x="11" y="18" width="26" height="12" rx="2" fill="none" stroke="#222" stroke-width="1.3"/><path d="M26 10l-6 8h6l-5 10" fill="none" stroke="#222" stroke-width="1.3"/></svg>
  <svg class="icon" style="left:254px;top:670px" viewBox="0 0 48 48"><circle cx="24" cy="24" r="22" fill="#fff" stroke="#222" stroke-width="1.5"/><path d="M2 24 A22 22 0 0 0 24 46" fill="none" stroke="#e31e3a" stroke-width="2.5"/><rect x="12" y="13" width="24" height="13" fill="none" stroke="#222" stroke-width="1.3"/><circle cx="19" cy="34" r="3" fill="none" stroke="#222" stroke-width="1.3"/><circle cx="29" cy="34" r="3" fill="none" stroke="#222" stroke-width="1.3"/><path d="M20 31l8-8M28 31l-8-8" stroke="#222" stroke-width="1.2"/></svg>

  <svg class="icon" style="left:509px;top:219px" viewBox="0 0 48 48"><circle cx="24" cy="24" r="22" fill="#fff" stroke="#222" stroke-width="1.5"/><path d="M2 24 A22 22 0 0 0 24 46" fill="none" stroke="#e31e3a" stroke-width="2.5"/><rect x="11" y="20" width="26" height="14" fill="none" stroke="#222" stroke-width="1.3"/><path d="M15 24h8M15 28h6M27 24h6v6h-6z" stroke="#222" stroke-width="1.2" fill="none"/><circle cx="30" cy="14" r="4" fill="none" stroke="#222" stroke-width="1.2"/></svg>
  <svg class="icon" style="left:509px;top:344px" viewBox="0 0 48 48"><circle cx="24" cy="24" r="22" fill="#fff" stroke="#222" stroke-width="1.5"/><path d="M2 24 A22 22 0 0 0 24 46" fill="none" stroke="#e31e3a" stroke-width="2.5"/><path d="M16 20l8-8 10 10-8 12-12-4z" fill="none" stroke="#222" stroke-width="1.3"/><circle cx="22" cy="22" r="2.5" fill="none" stroke="#222" stroke-width="1.2"/></svg>
  <svg class="icon" style="left:509px;top:428px" viewBox="0 0 48 48"><circle cx="24" cy="24" r="22" fill="#fff" stroke="#222" stroke-width="1.5"/><path d="M2 24 A22 22 0 0 0 24 46" fill="none" stroke="#e31e3a" stroke-width="2.5"/><rect x="17" y="11" width="14" height="24" rx="2" fill="none" stroke="#222" stroke-width="1.3"/><rect x="20" y="16" width="4" height="4" fill="none" stroke="#222"/><rect x="25" y="16" width="4" height="4" fill="none" stroke="#222"/><rect x="20" y="22" width="4" height="4" fill="none" stroke="#222"/></svg>
  <svg class="icon" style="left:509px;top:519px" viewBox="0 0 48 48"><circle cx="24" cy="24" r="22" fill="#fff" stroke="#222" stroke-width="1.5"/><path d="M2 24 A22 22 0 0 0 24 46" fill="none" stroke="#e31e3a" stroke-width="2.5"/><path d="M13 36V16h8v20M21 36V22h7v14M28 36v-9h7v9z" fill="none" stroke="#222" stroke-width="1.3"/></svg>
  <svg class="icon" style="left:509px;top:583px" viewBox="0 0 48 48"><circle cx="24" cy="24" r="22" fill="#fff" stroke="#222" stroke-width="1.5"/><path d="M2 24 A22 22 0 0 0 24 46" fill="none" stroke="#e31e3a" stroke-width="2.5"/><circle cx="24" cy="24" r="9" fill="none" stroke="#222" stroke-width="1.4" stroke-dasharray="4 2"/><circle cx="24" cy="24" r="4" fill="none" stroke="#222" stroke-width="1.3"/></svg>

  <p class="perk left" style="top:225px">Are capable of making price changes in a matter of seconds. This allows for swiftly adapting to pricing updates in today’s volatile market</p>
  <p class="perk left" style="top:308px">Can reallocate up to 10.7 labor hours per week, or over 550 hours annually.&nbsp; This eliminates the need for repetitive paper printing while reducing ink and administrative expenses.</p>
  <p class="perk left" style="top:402px">Improve the accuracy of prices 10 fold over the traditional paper process.&nbsp; This helps proactively address the issues of missed hotsheets in the day-to-day operations.</p>
  <p class="perk left" style="top:501px">Shift Store Associate focus from the monotony of putting up and taking down labels to sales building initiatives, increasing staff morale</p>
  <p class="perk left" style="top:587px">Provide capabilities to ‘flash’ on demand. This is leveraged by staff for finding and stocking products quicker on the sales floor, thereby reducing put-away errors.</p>
  <p class="perk" style="left:310px;top:687px;width:462px">Minimize lost sales.&nbsp; ESSLs know when quantity on hand has reached zero, and inform the customer to ask for a sales associate to special order the product.</p>

  <p class="perk right" style="top:225px">Are smart enough to know which items are on sales (i.e. MIP based promotions) and then adapt to display the regular and sales price, including calling out it savings. This makes it substantially easier to execute short sales promotions.</p>
  <p class="perk right" style="top:349px">Without store associate intervention, automatically give a different look and feel to labels that are MSU, closeout, and consumer unit based tags</p>
  <p class="perk right" style="top:433px">Come QR code ready, allowing shoppers the ability to scan products to receive insightful content about its features. Think grills, power equipment, and other products benefiting from POP.</p>
  <p class="perk right" style="top:529px">Provide modernized look and feel, available in 4 color bin label templates</p>
  <p class="perk right" style="top:592px">Have direct compatibility with your current Norvik devices (e.g. NX40)</p>

  <h2 class="abs h-costs">Program Costs</h2>
  <h3 class="abs h-pricing">Pricing</h3>

  <svg class="string" style="top:309px" viewBox="0 0 22 30"><path d="M20 24 C8 22 2 14 4 6 C6 0 14 2 14 10 L17 22" fill="none" stroke="#222" stroke-width="1"/></svg>
  <div class="tag" style="top:321px">1.5” tags = $6.51</div>
  <div class="caption" style="top:349px">(smaller tag for tight spaces)</div>
  <svg class="string" style="top:358px" viewBox="0 0 22 30"><path d="M20 24 C8 22 2 14 4 6 C6 0 14 2 14 10 L17 22" fill="none" stroke="#222" stroke-width="1"/></svg>
  <div class="tag" style="top:370px">2.1” tags = $7.12</div>
  <div class="caption" style="top:399px">(most typically used)</div>
  <svg class="string" style="top:404px" viewBox="0 0 22 30"><path d="M20 24 C8 22 2 14 4 6 C6 0 14 2 14 10 L17 22" fill="none" stroke="#222" stroke-width="1"/></svg>
  <div class="tag" style="top:416px">4.2” tags = $15.62</div>
  <svg class="string" style="top:441px" viewBox="0 0 22 30"><path d="M20 24 C8 22 2 14 4 6 C6 0 14 2 14 10 L17 22" fill="none" stroke="#222" stroke-width="1"/></svg>
  <div class="tag" style="top:453px">7.4” tags = $35.24</div>

  <h3 class="abs h-extra">In addition to the initial purchase:</h3>
  <ul class="abs checks">
    <li>Fixturing for tags are required</li>
    <li>Monthly SAAS fee (includes support, software, dashboards, etc.) are:
      <ul class="sub">
        <li>Less than 10,000 tags = $100 a month</li>
        <li>Greater or equal to 10,000 tags = $200 a month</li>
        <li>Additional benefits available for retailers with 10 or more stores</li>
      </ul>
    </li>
  </ul>

  <h2 class="abs h-touch">Get in Touch to Discover More</h2>
  <div class="contact-title" style="top:866px">Qelmar Group Sales Rep</div>
  <div class="contact-line" style="top:886px"><svg viewBox="0 0 10 10"><path d="M2 1l2 2-1 1.5c.8 1.3 1.7 2.2 3 3L7.5 6l2 2-1 1.5C5 9 1 5 .5 1.5z" fill="#222"/></svg>555.014.2286</div>
  <div class="contact-line" style="top:900px"><svg viewBox="0 0 10 10"><rect x=".5" y="2" width="9" height="6" fill="none" stroke="#222"/><path d="M.5 2l4.5 3.5L9.5 2" fill="none" stroke="#222"/></svg>m.harlow@qelmar.com</div>
  <div class="contact-title" style="top:922px">Birch Toolworks Contacts</div>
  <div class="contact-line" style="top:942px"><svg viewBox="0 0 10 10"><path d="M2 1l2 2-1 1.5c.8 1.3 1.7 2.2 3 3L7.5 6l2 2-1 1.5C5 9 1 5 .5 1.5z" fill="#222"/></svg>555.019.7730</div>
  <div class="contact-line" style="top:956px"><svg viewBox="0 0 10 10"><rect x=".5" y="2" width="9" height="6" fill="none" stroke="#222"/><path d="M.5 2l4.5 3.5L9.5 2" fill="none" stroke="#222"/></svg>storeops@birchtoolworks.com</div>

  <h2 class="abs h-start">Getting Started</h2>
  <div class="start-rule"><span></span></div>

  <div class="step" style="left:263px;top:794px;width:234px;height:61px">Complete the discovery survey</div>
  <div class="step" style="left:263px;top:864px;width:234px;height:102px">Have a general understanding of the number of ESLs you’d like to implement, types of fixtures you currently use and approximate timetable for readiness</div>
  <div class="step" style="left:517px;top:795px;width:234px;height:82px">Qelmar Group will contact you within 48 hours of completing the above discovery survey for an exploratory call</div>
  <div class="step" style="left:517px;top:885px;width:234px;height:83px">Following the exploratory call, Qelmar Group will provide a high-level quote and an understanding of next steps</div>

  <svg class="step-check" style="left:254px;top:815px" viewBox="0 0 17 17"><circle cx="8.5" cy="8.5" r="8.5" fill="#e31e3a"/><path d="M4.5 8.5l3 3 5-6" fill="none" stroke="#fff" stroke-width="1.8"/></svg>
  <svg class="step-check" style="left:254px;top:884px" viewBox="0 0 17 17"><circle cx="8.5" cy="8.5" r="8.5" fill="#e31e3a"/><path d="M4.5 8.5l3 3 5-6" fill="none" stroke="#fff" stroke-width="1.8"/></svg>
  <svg class="step-check" style="left:508px;top:815px" viewBox="0 0 17 17"><circle cx="8.5" cy="8.5" r="8.5" fill="#e31e3a"/><path d="M4.5 8.5l3 3 5-6" fill="none" stroke="#fff" stroke-width="1.8"/></svg>
  <svg class="step-check" style="left:508px;top:905px" viewBox="0 0 17 17"><circle cx="8.5" cy="8.5" r="8.5" fill="#e31e3a"/><path d="M4.5 8.5l3 3 5-6" fill="none" stroke="#fff" stroke-width="1.8"/></svg>
</div>
</body>
</html>
```